Typing Service Business Card Design

Need a new business card design for new logo update. The Ledger Scribes is an outsourced typing service. We type audio / voice files into word documents. We are a professional service that is recognised in the industry over the past 15 years and have a strong connection to our brand. The final design should be professional, simple, yet effective.

Corinna Waldrop
Director

corinna@lsx.com.au
www.theledgerscribes.com.au

```html
<!DOCTYPE html>
<html lang="en">
<head>
<meta charset="utf-8">
<title>The Ledger Scribes – Business Card</title>
<link rel="stylesheet" href="https://fonts.googleapis.com/css2?family=Jost:wght@300;400;600&display=swap">
<style>
  :root {
    --stage: #1d1d1d;
    --card: #050505;
    --pink: #e0459e;
    --white: #f2f2f2;
    --rule: #3a3a3a;
  }
  * { box-sizing: border-box; margin: 0; padding: 0; }
  html, body {
    width: 1200px; height: 900px; overflow: hidden;
    background: var(--stage);
    font-family: "Jost", "Futura", sans-serif;
  }
  .canvas {
    width: 1200px; height: 900px;
    display: flex; justify-content: center; align-items: center; gap: 60px;
  }
  .card {
    position: relative;
    width: 360px; height: 590px;
    background: var(--card);
    border-radius: 26px;
  }
  .card::before {
    content: "";
    position: absolute; inset: 10px;
    border: 2px solid var(--pink);
    border-radius: 20px;
  }
  .contact {
    position: absolute; left: 0; right: 0; top: 250px;
    text-align: center; color: var(--white);
  }
  .contact .name {
    color: var(--pink); font-weight: 600; font-size: 27px; letter-spacing: 0.3px;
  }
  .contact .role {
    font-weight: 400; font-size: 16px; margin-top: 2px;
  }
  .icon-row {
    display: flex; justify-content: center; align-items: center;
    margin: 20px auto 22px; width: 150px; position: relative;
  }
  .icon-row::before {
    content: ""; position: absolute; left: 0; right: 0; top: 50%;
    border-top: 1px solid var(--pink);
  }
  .icon-row svg { position: relative; margin: 0 5px; background: var(--card); border-radius: 50%; }
  .contact .details { font-weight: 300; font-size: 18px; line-height: 1.3; }
  .brand {
    position: absolute; left: 30px; right: 30px; top: 255px;
  }
  .brand .wordmark {
    display: flex; align-items: center; gap: 10px;
    color: var(--pink); font-weight: 600; font-size: 26px;
  }
  .brand .wordmark .mark {
    width: 14px; height: 14px; background: var(--pink);
  }
  .brand .tagline {
    text-align: right; color: var(--white);
    font-weight: 400; font-size: 16px; margin-top: 4px;
  }
  .brand .rule {
    border-top: 1px solid var(--rule); margin-top: 10px;
  }
</style>
</head>
<body>
<main class="canvas">
  <section class="card card-front">
    <div class="contact">
      <h1 class="name">Corinna Waldrop</h1>
      <p class="role">Director</p>
      <div class="icon-row">
        <svg width="26" height="26" viewBox="0 0 26 26" aria-label="Email">
          <circle cx="13" cy="13" r="12" fill="none" stroke="#e0459e" stroke-width="1.5"/>
          <rect x="7" y="9" width="12" height="8" fill="#e0459e"/>
          <path d="M7 9 L13 14 L19 9" fill="none" stroke="#050505" stroke-width="1.2"/>
        </svg>
        <svg width="26" height="26" viewBox="0 0 26 26" aria-label="Web">
          <circle cx="13" cy="13" r="12" fill="none" stroke="#e0459e" stroke-width="1.5"/>
          <circle cx="13" cy="13" r="6" fill="none" stroke="#e0459e" stroke-width="1.5"/>
          <path d="M7 13 H19 M13 7 V19" stroke="#e0459e" stroke-width="1.2"/>
        </svg>
      </div>
      <p class="details">corinna@lsx.com.au<br>www.theledgerscribes.com.au</p>
    </div>
  </section>
  <section class="card card-back">
    <div class="brand">
      <div class="wordmark"><span class="mark"></span>The Ledger Scribes</div>
      <p class="tagline">You speak. We write.</p>
      <div class="rule"></div>
    </div>
  </section>
</main>
</body>
</html>
```